New Coffee Shop business card

We are opening our new coffee shop and are needing business cards to take with us on February 6th to Atlanta, Ga to a show.

We will be offering the following menu type items:

coffee
teas
espresso
frappes
smoothies

sandwiches
soups
salads
pastries
ice cream

Our shop is in a rural country-side area and we would like to convey that feel in our shop. In addition to the cafe we will also be selling gifts and furniture and other home decor. Much of this merchandise will be rescued, refurbished or repurposed which is also a core value of what we are all about.

We have a company logo we would like incorporated into the design.

We will also provide files that have the elements of the logo which may also be useful in the design of the card.

Since we are not open yet we need one slightly altered version of the card as well as the final product which states "Opening in the summer 2015"

Target Market(s)

moderate to slightly upscale and folksy.

Industry/Entity Type

Coffee Shop

Contact Information for Business Card

Fern Hollow Coffee
name
address
phone number
email

Card

Font styles to use
Sans Serif

Requirements
Must have
• Must include Logo
• Must include information on menu.
• Must include information on our merchandise sales as described inthe project description.
• Color scheme to complement the logo
Nice to have
• The following descriptions
• "We are also selling gifts, furniture, and other home decoration."
• "We rescue, refurbish, and repurpose old furniture so it can live again."

```html
<!DOCTYPE html>
<html lang="en">
<head>
<meta charset="utf-8">
<title>Fern Hollow — Cafe Menu Card</title>
<link rel="stylesheet" href="https://fonts.googleapis.com/css2?family=Federo&family=Comfortaa:wght@400&family=Open+Sans:wght@400&display=swap">
<style>
  :root {
    --paper: #ffffff;
    --brand-red: #861a19;
    --brand-red-deep: #7a1615;
    --ink: #111111;
    --cream: #f4e7d2;
    --menu-text: #ffffff;
    --steam: #a0514a;
    --cup: #6f3a33;
  }
  * { margin: 0; padding: 0; box-sizing: border-box; }
  html, body { width: 1200px; height: 2273px; overflow: hidden; background: var(--paper); }
  .card { position: relative; width: 1200px; height: 2273px; background: var(--paper); }

  .brand-header { position: absolute; left: 0; top: 0; width: 1200px; height: 535px; text-align: center; }
  .brand-name {
    font-family: "Federo", sans-serif; font-weight: 400; color: var(--brand-red);
    font-size: 222px; line-height: 1; letter-spacing: 2px; margin-top: 8px; white-space: nowrap;
  }
  .brand-offer {
    font-family: "Comfortaa", sans-serif; color: var(--ink);
    font-size: 84px; line-height: 140px; margin-top: 6px;
  }

  .menu-panel {
    position: absolute; left: 0; top: 535px; width: 1200px; height: 1715px;
    background: var(--brand-red); border-top: 8px solid var(--paper);
  }
  .menu-heading {
    position: absolute; left: 0; top: 120px; width: 1200px; text-align: center;
    font-family: "Federo", sans-serif; color: var(--cream); font-size: 112px; line-height: 1;
  }
  .flourish { position: absolute; top: 150px; width: 370px; height: 50px; }
  .flourish--left { left: 20px; }
  .flourish--right { right: 20px; }

  .menu-list {
    position: absolute; top: 330px; list-style: none;
    font-family: "Open Sans", sans-serif; color: var(--menu-text);
    font-size: 92px; line-height: 136px;
  }
  .menu-list--drinks { left: 40px; }
  .menu-list--food { right: 12px; text-align: right; }

  .coffee-cup { position: absolute; left: 440px; top: 1160px; width: 320px; height: 555px; }
</style>
</head>
<body>
<main class="card">
  <header class="brand-header">
    <h1 class="brand-name">Fern Hollow</h1>
    <p class="brand-offer">Cafe, Gifts, Furniture<br>&amp; Home Decor.</p>
  </header>

  <section class="menu-panel" aria-labelledby="menu-title">
    <svg class="flourish flourish--left" viewBox="0 0 370 50" role="img" aria-label="Decorative scroll flourish">
      <rect x="0" y="22" width="370" height="6" rx="3" fill="var(--cream)" opacity="0.85"/>
    </svg>
    <h2 class="menu-heading" id="menu-title">Menu</h2>
    <svg class="flourish flourish--right" viewBox="0 0 370 50" role="img" aria-label="Decorative scroll flourish">
      <rect x="0" y="22" width="370" height="6" rx="3" fill="var(--cream)" opacity="0.85"/>
    </svg>

    <ul class="menu-list menu-list--drinks">
      <li>Coffee</li>
      <li>Espresso</li>
      <li>Frappes</li>
      <li>Teas</li>
      <li>Smoothies</li>
    </ul>
    <ul class="menu-list menu-list--food">
      <li>Sandwiches</li>
      <li>Soups</li>
      <li>Salads</li>
      <li>Pastries</li>
      <li>Ice Cream</li>
    </ul>

    <svg class="coffee-cup" viewBox="0 0 320 555" role="img" aria-label="Illustration of a steaming coffee cup on a saucer">
      <defs>
        <linearGradient id="cup-tone" x1="0" y1="0" x2="0" y2="1">
          <stop offset="0" stop-color="var(--steam)" stop-opacity="0.35"/>
          <stop offset="1" stop-color="var(--cup)" stop-opacity="0.9"/>
        </linearGradient>
      </defs>
      <rect x="0" y="0" width="320" height="555" rx="40" fill="url(#cup-tone)"/>
    </svg>
  </section>
</main>
</body>
</html>
```